pathology learning flashcard template graphic design .

Creative designs for 2 sides of the flashcards to include colorful sectioning and font sizes that will make it easy to use in studying.

```html
<!DOCTYPE html>
<html lang="en">
<head>
<meta charset="UTF-8">
<title>Pathology Flashcard – Achalasia</title>
<link href="https://fonts.googleapis.com/css2?family=Montserrat:wght@700&family=Nunito+Sans:wght@400;700&family=Roboto+Condensed:ital,wght@1,300;1,400&display=swap" rel="stylesheet">
<style>
  :root {
    --rose: #ea5370;
    --rose-deep: #dc3f5f;
    --ink: #222222;
    --note-bg: #eadbd6;
    --note-shadow: #f3b3b4;
    --note-title: #b1393f;
    --note-text: #c0443f;
    --source: #f19aa5;
    --paper: #ffffff;
  }
  * { margin: 0; padding: 0; box-sizing: border-box; }
  html, body { width: 1200px; height: 823px; overflow: hidden; background: var(--paper); }
  .card { position: relative; width: 1200px; height: 823px; background: var(--paper); font-family: "Nunito Sans", "Helvetica Neue", sans-serif; color: var(--ink); }

  .category-band { position: absolute; left: 0; top: 0; width: 513px; height: 124px; background: var(--rose); }
  .category-title { position: absolute; left: 56px; top: 70px; font-family: "Montserrat", sans-serif; font-weight: 700; font-size: 41px; line-height: 1; color: var(--paper); letter-spacing: 0.5px; }
  .topic-title { position: absolute; left: 0; width: 513px; top: 142px; text-align: center; font-family: "Montserrat", sans-serif; font-weight: 700; font-size: 43px; line-height: 1; color: var(--rose); letter-spacing: 0.5px; }

  .section-label { position: absolute; left: 57px; font-family: "Montserrat", sans-serif; font-weight: 700; font-size: 22px; line-height: 1; color: var(--rose-deep); }
  .section-body { position: absolute; left: 57px; font-size: 25px; line-height: 32px; color: var(--ink); }

  .label-definition { top: 229px; }
  .body-definition { top: 256px; }
  .label-etiology { top: 376px; }
  .body-etiology { top: 403px; }

  .symptom-pill { position: absolute; left: 56px; top: 579px; width: 264px; height: 38px; border-radius: 7px; background: var(--rose); color: var(--paper); font-family: "Montserrat", sans-serif; font-weight: 700; font-size: 21px; line-height: 38px; padding-left: 9px; }
  .body-symptoms { top: 623px; color: var(--rose); }

  .clinical-block { position: absolute; left: 548px; font-size: 25px; line-height: 32px; color: var(--ink); }
  .clinical-block .tag { font-family: "Montserrat", sans-serif; font-weight: 700; color: var(--rose-deep); font-size: 23px; }
  .block-dx { top: 53px; }
  .block-rx { top: 265px; }

  .answer-note { position: absolute; left: 547px; top: 438px; width: 620px; height: 347px; }
  .answer-note svg { position: absolute; left: 0; top: 0; }
  .answer-title { position: absolute; left: 27px; top: 20px; font-family: "Montserrat", sans-serif; font-weight: 700; font-size: 24px; line-height: 1; color: var(--note-title); }
  .answer-text { position: absolute; left: 27px; top: 53px; font-family: "Roboto Condensed", "Arial Narrow", sans-serif; font-style: italic; font-weight: 300; font-size: 23.5px; line-height: 30px; color: var(--note-text); white-space: nowrap; }

  .sources { position: absolute; right: 48px; top: 797px; font-size: 12.5px; line-height: 1; color: var(--source); }
</style>
</head>
<body>
<main class="card">
  <div class="category-band"></div>
  <h1 class="category-title">GASTROINTESTINAL</h1>
  <h2 class="topic-title">ACHALASIA</h2>

  <h3 class="section-label label-definition">Definition:</h3>
  <p class="section-body body-definition">Motility disorder where esophageal<br>relaxation is impaired in the lower<br>esophageal sphincter (LES).</p>

  <h3 class="section-label label-etiology">Etiology/Pathology:</h3>
  <p class="section-body body-etiology">Destruction of inhibitory neurons<br>in the Auerbach plexus. Loss of<br>peristalsis in the lower esophageal<br>sphincter (Lower-two thirds of the<br>esophagus).</p>

  <div class="symptom-pill">P/E and Symptoms:</div>
  <p class="section-body body-symptoms">Dysphagia that is progressive,<br>regurgitation, weight-loss, dry cough,<br>chest pain, GERD, esophageal<br>perforation, squamous cell<br>carcinoma, aspiration pneumonia.</p>

  <p class="clinical-block block-dx"><span class="tag">Dx:</span> Barium swallow will show ‘bird’s beak’ and<br>esophageal dilation. Manometry will present with<br>increased resting lower esophageal sphincter pressure.<br>Endoscopy will usually present with normal mucosa<br>and LES dilation, and in some cases residual material<br>such as undigested food particles may be present.</p>

  <p class="clinical-block block-rx"><span class="tag">Rx:</span> First line of treatment are nitrates, calcium channel<br>blockers, and Botulinum toxin injection in the LES.<br>Long term management options include esophageal<br>dilation with pneumatic balloon and myotomy.</p>

  <section class="answer-note">
    <svg width="620" height="347" viewBox="0 0 620 347" aria-hidden="true">
      <rect x="0" y="14" width="613" height="332" rx="9" fill="var(--note-shadow)"/>
      <rect x="7" y="0" width="612" height="338" rx="9" fill="var(--note-bg)"/>
    </svg>
    <h4 class="answer-title">C- Achalasia</h4>
    <p class="answer-text">Symptoms and studies suggestive of achalasia. Patient’s<br>manometry presents with no relaxation of the lower<br>esophageal sphincter during swallowing. Patient also<br>complains of dysphagia and is unable to swallow properly,<br>leading to weight loss. Patient has no past infection or<br>inflammation, ruling out eosinophilic esophagitis. Patient<br>does not have chronic GERD, eliminating the possibility of<br>Barrett esophagus, in which at least 5 years of acid reflux are<br>beforehand to develop columnar metaplasia.</p>
  </section>

  <p class="sources">Sources: Hartwell’s Drug Guide; Pellmore Pocket Formulary; Medirefs.net; Clinipedia.org</p>
</main>
</body>
</html>
```